Halvorin Law Estate Planning focusing on families with minor children, November Thanksgiving Theme

POSTCARD Size: height 152 mm x width 279 mm.

Our logo can be found in the attachments and the text to be used in the postcard.

We are an Estate Planning Law Firm that focuses on Families with Minor Children. We are sending out a mailing piece, via every door direct mail, at the end of October to incentivize potential clients to call and schedule appointments in November.

We would like the design to use the traditional US fall colors. The final design should blend the difficult task of fun (we are dealing with kids) and professional (we are a law firm). We have included the text we want to use to help with the understanding of our goal.

- Please include different textual layers to the post card, including some text boxes as well.
- Photo of children in a Thanksgiving setting.
Updates

This is for a post card, dimensions height 152 mm x width 279 mm. Added Tuesday, September 15, 2015

Target Market(s)

Families with Young Children

Industry/Entity Type

Law Firm

Font styles to use
Sans Serif

Requirements
Must have
• All the text provided and the colors mentioned in the project description.
• Must fit a postcard with dimensions height 152 mm x width 279 mm.
Nice to have
• Different textual layers to the post card, including some text boxes as well.
• Photo of children in a Thanksgiving setting.

```html
<!DOCTYPE html>
<html lang="en">
<head>
<meta charset="utf-8">
<title>Halvorin Law – Thanksgiving Postcard</title>
<link href="https://fonts.googleapis.com/css2?family=Arimo:wght@400;700&display=swap" rel="stylesheet">
<style>
  :root{
    --page:#e4e1da;
    --card:#ffffff;
    --olive:#8c9b38;
    --olive-dark:#6d7b26;
    --text:#5a5a52;
    --ink:#2f2f2a;
    --accent:#d8772a;
    --rule:#b9b9b0;
  }
  *{box-sizing:border-box;margin:0;padding:0}
  html,body{width:900px;height:1200px;overflow:hidden}
  body{background:var(--page);font-family:"Arimo",Arial,sans-serif;color:var(--text);position:relative}
  .card{position:absolute;left:54px;width:792px;height:546px;background:var(--card);box-shadow:0 4px 14px rgba(0,0,0,.18);overflow:hidden}
  .front{top:24px}
  .back{top:612px;height:564px}

  .brand{position:absolute;font-weight:400;color:var(--text);font-size:21px}
  .front .brand{left:70px;top:28px}

  .front-intro{position:absolute;left:22px;top:78px;width:240px}
  .headline{color:var(--olive-dark);font-weight:700;font-size:19px;line-height:1.2;margin-bottom:16px}
  .lede{font-size:16.5px;line-height:1.32;color:var(--olive)}

  .hero-photo{position:absolute;left:285px;top:0;width:507px;height:330px;background:linear-gradient(135deg,#d9c7a6,#c6a77c 55%,#9a8a5a)}
  .offer-panel{position:absolute;left:285px;top:330px;width:507px;height:216px;background:var(--olive)}
  .advisor-photo{position:absolute;left:14px;top:12px;width:62px;height:66px;background:linear-gradient(160deg,#c9b59a,#7b6b56)}
  .offer-text{position:absolute;left:88px;top:12px;right:16px;color:#fff;font-size:15.5px;line-height:1.25}
  .offer-text .donate{background:var(--accent);padding:0 3px;font-weight:700}
  .story{position:absolute;left:14px;right:16px;top:90px;font-size:13.4px;line-height:1.28;color:#fff}

  .session{position:absolute;left:26px;top:22px;width:440px}
  .session h2{font-size:19px;line-height:1.2;color:var(--ink);font-weight:700;margin-bottom:12px}
  .benefits{list-style:none}
  .benefits li{position:relative;padding-left:22px;margin-bottom:10px;font-size:16px;line-height:1.25;color:var(--olive)}
  .benefits li::before{content:"";position:absolute;left:0;top:4px;width:11px;height:11px;background:var(--olive)}
  .contact{position:absolute;left:84px;top:396px;font-size:16px;line-height:1.3;color:var(--text);font-style:normal}
  .contact .call{color:var(--olive-dark);margin-top:14px}
  .back .brand{left:540px;top:488px}
  .divider{position:absolute;left:480px;top:36px;width:1px;height:410px;background:var(--rule)}
  .stamp{position:absolute;left:690px;top:30px;width:72px;height:84px;border:1px solid var(--rule)}
  .address-lines{position:absolute;left:520px;top:190px;width:250px}
  .address-lines span{display:block;height:1px;background:var(--rule);margin-bottom:34px}
</style>
</head>
<body>

<section class="card front">
  <div class="brand">Halvorin Law</div>
  <div class="front-intro">
    <h1 class="headline">A Gift Your Family Will Thank You For... For Generations To Come</h1>
    <p class="lede">Here's something important you need to know that directly affects your family: If you want to protect your assets and make sure your kids are taken care of by people you LOVE if the unthinkable should happen to you and your spouse... then you must PLAN NOW! Planning now is one of the greatest gifts you can give to your loved ones.</p>
  </div>
  <div class="hero-photo" role="img" aria-label="Photo of a smiling young girl in a Thanksgiving setting"></div>
  <div class="offer-panel">
    <div class="advisor-photo" role="img" aria-label="Portrait of the family advisor"></div>
    <p class="offer-text">Make An Appointment In November For A Family Strategy Session And You'll Get the Session for FREE, Plus I'll <span class="donate">Donate $50</span> To The Eastbrook Food Bank In Your Name!</p>
    <p class="story">My name is Marcus Halvorin. I'm your neighborhood Family Advisor and I have much to be thankful for, especially being able to serve the Eastbrook community. As my way of giving back and saying thank you, not only I am going to help you and your family but also help the less fortunate members of our community during this Thanksgiving season.</p>
  </div>
</section>

<section class="card back">
  <div class="session">
    <h2>During Your FREE Strategy Session You And Your Spouse Will:</h2>
    <ul class="benefits">
      <li>Choose the Right Guardians for Your Kids and Avoid Making the Six Common Mistakes!</li>
      <li>Get Your Financial House in Order and Keep it that Way!</li>
      <li>Ensure Your Kids (&amp; Spouse) Are Prepared for Life Without You!</li>
      <li>Discover How To Legally Avoid ALL Estate Taxes &amp; Keep Your Family Out of Court!</li>
      <li>Learn the Secret to Protecting Your Kids from their Inheritance!</li>
      <li>Discover How to Leave Your Loved Ones a Gift Far Greater Than All the Money in the World!</li>
    </ul>
  </div>
  <address class="contact">
    Halvorin Law, PLLC<br>
    48 Linden Row Street<br>
    Eastbrook, ID 83700<br>
    www.halvorinlaw.com
    <p class="call">Call 208-555-0147 to make your appointment</p>
  </address>
  <div class="divider"></div>
  <div class="stamp"></div>
  <div class="address-lines"><span></span><span></span><span></span><span></span></div>
  <div class="brand">Halvorin Law</div>
</section>

</body>
</html>
```